Sleek business card design for digital agency.

Brief document attached for detailed description and inspiration. Looking for a minimalist sleek, cool, modern business card design.

Industry/Entity Type

Digital

```html
<!DOCTYPE html>
<html lang="en">
<head>
<meta charset="utf-8">
<title>Nimbus Labs – Business Card</title>
<link rel="stylesheet" href="https://fonts.googleapis.com/css2?family=Tinos&display=swap">
<style>
  :root {
    --page-bg: #e9e7e3;
    --card-white: #ffffff;
    --ink-dark: #3a3a3a;
    --back-black: #050505;
    --back-grey: #8a8a8a;
    --back-text: #f2f2f2;
    --rule: #d8d8d8;
    --shadow: rgba(0, 0, 0, 0.18);
  }
  * { box-sizing: border-box; margin: 0; padding: 0; }
  html, body {
    width: 1200px;
    height: 1200px;
    overflow: hidden;
    background: var(--page-bg);
    font-family: "Tinos", "Times New Roman", serif;
  }
  .canvas {
    position: relative;
    width: 1200px;
    height: 1200px;
  }
  .card {
    position: absolute;
    left: 150px;
    width: 900px;
    height: 514px;
    box-shadow: 0 6px 20px var(--shadow);
  }
  .card--front {
    top: 56px;
    background: var(--card-white);
    display: flex;
    align-items: center;
    justify-content: center;
    gap: 34px;
  }
  .brand-dot {
    width: 96px;
    height: 96px;
    border-radius: 50%;
    background: var(--ink-dark);
  }
  .brand-name {
    font-size: 112px;
    color: var(--ink-dark);
    font-weight: 400;
    letter-spacing: 1px;
  }
  .card--back {
    top: 630px;
    background: linear-gradient(160deg, var(--back-black) 0%, var(--back-black) 35%, var(--back-grey) 100%);
    color: var(--back-text);
  }
  .back-line { position: absolute; white-space: nowrap; }
  .person-name { left: 36px; top: 30px; font-size: 38px; }
  .person-title { left: 36px; top: 76px; font-size: 22px; }
  .header-rule {
    position: absolute;
    left: 36px;
    right: 36px;
    top: 112px;
    height: 0;
    border-top: 2px solid var(--rule);
  }
  .drink-order { left: 36px; top: 150px; font-size: 22px; }
  .email { left: 36px; top: 262px; font-size: 22px; }
  .web { left: 36px; top: 294px; font-size: 22px; }
  .address-1 { left: 560px; top: 150px; font-size: 22px; }
  .address-2 { left: 560px; top: 182px; font-size: 22px; }
  .phone-mobile { left: 560px; top: 262px; font-size: 22px; }
  .phone-office { left: 560px; top: 294px; font-size: 22px; }
</style>
</head>
<body>
<main class="canvas">
  <section class="card card--front" aria-label="Card front">
    <span class="brand-dot" aria-hidden="true"></span>
    <span class="brand-name">Nimbus Labs</span>
  </section>

  <section class="card card--back" aria-label="Card back">
    <p class="back-line person-name">Daniel Reeve</p>
    <p class="back-line person-title">Marketing Director</p>
    <div class="header-rule"></div>
    <p class="back-line drink-order">Drink Order: G&amp;T with cucumber</p>
    <p class="back-line email">dreeve@nimbuslabs.com</p>
    <p class="back-line web">nimbuslabs.com/social</p>
    <p class="back-line address-1">Level 2, 18 Harlow St.</p>
    <p class="back-line address-2">Eastbrook NSW 5010</p>
    <p class="back-line phone-mobile">0400 100 234</p>
    <p class="back-line phone-office">03 9000 4567</p>
  </section>
</main>
</body>
</html>
```